Business Card Design for Event Planning Company

Create a business card for event planning company using our new logo. After I pick the design, I will need files made for 6 employees. Our company provides event design & logistics services as well as venue management. The font should be sans serif and complementary to the logo. I will need to know the name of the font selected for the final design. The phone numbers listed should be separated by "." not "-"

Address for the card
PO Box 318, Washington, DC 20019

Card One
Lorna Pettibone
lpettibone@galavoyant.com
202.481.7730

Card Two
Miriam Okonkwo
mokonkwo@galavoyant.com
202.556.2047

Card Three
Tessa Varnholt
tvarnholt@galavoyant.com
978.620.4471

Card Four
Robin Fess
rfess@galavoyant.com
202.718.3362

Card Five
Ada-Rose Pelletan-Uzor
adarose@galavoyant.com
202.839.1205

Card Six
Beatrix Holloway
Beatrix@galavoyant.com
202.492.6618

Target Market(s)

Corporate/Non-Profit

Industry/Entity Type

Event Planning

Contact Information for Business Card

Address for the card

Card One
Lorna Pettibone
lpettibone@galavoyant.com
202.481.7730

Card Two
Miriam Okonkwo
202.556.2047

Card Three
Tessa Varnholt
978.620.4471

Card Four
Robin Fess
rfess@galavoyant.com
202.718.3362

Card Five
Ada-Rose Pelletan-Uzor
202.839.1205

Card Six
Beatrix Holloway
202.492.6618

Font styles to use
Sans Serif

Colors

Designer to choose colors to be used in the design.

Requirements
Must have
• Two-sided with logo
Should not have
• Extra colors or be too busy

```html
<!DOCTYPE html>
<html lang="en">
<head>
<meta charset="UTF-8">
<title>Galavoyant Business Card</title>
<link href="https://fonts.googleapis.com/css2?family=Work+Sans:wght@300;400;700&display=swap" rel="stylesheet">
<style>
  :root {
    --page-bg: #2b2b2e;
    --card-bg: #161618;
    --ink-white: #f2f2f2;
    --ink-teal: #5fa9a8;
    --silver-light: #e4e4e4;
    --silver-mid: #8d8d8f;
    --silver-dark: #2a2a2c;
  }
  * { box-sizing: border-box; margin: 0; padding: 0; }
  html, body {
    width: 1200px;
    height: 900px;
    overflow: hidden;
    background: var(--page-bg);
    font-family: "Work Sans", sans-serif;
  }
  .card {
    position: absolute;
    left: 250px;
    width: 700px;
    height: 400px;
    background: var(--card-bg);
    overflow: hidden;
    box-shadow: 0 10px 30px rgba(0,0,0,0.35);
  }
  .card--front { top: 30px; }
  .card--back { top: 470px; }

  .mark-decoration {
    position: absolute;
    top: 0;
    height: 100%;
  }
  .card--front .mark-decoration {
    left: 0;
    width: 380px;
    background: linear-gradient(100deg, var(--silver-dark) 0%, var(--silver-mid) 55%, var(--silver-light) 100%);
  }
  .card--back .mark-decoration {
    right: 0;
    width: 300px;
    background: linear-gradient(100deg, var(--silver-dark) 0%, var(--silver-mid) 45%, var(--silver-light) 100%);
  }

  .wordmark {
    position: absolute;
    font-weight: 300;
    color: var(--ink-white);
    letter-spacing: 0.5px;
    line-height: 1;
  }
  .card--front .wordmark {
    left: 440px;
    top: 200px;
    font-size: 38px;
    display: flex;
    align-items: center;
    gap: 12px;
  }
  .wordmark__dot {
    width: 14px;
    height: 14px;
    border-radius: 50%;
    background: var(--ink-white);
  }
  .card--back .wordmark {
    left: 48px;
    top: 46px;
    font-size: 42px;
  }

  .contact {
    position: absolute;
    left: 62px;
    top: 178px;
    color: var(--ink-white);
  }
  .contact__name {
    font-size: 25px;
    font-weight: 700;
    letter-spacing: 1px;
    text-transform: uppercase;
    margin-bottom: 12px;
  }
  .contact__name-last { color: var(--ink-teal); }
  .contact__line {
    font-size: 18px;
    font-weight: 400;
    line-height: 1.45;
  }
  .contact__row {
    display: flex;
    align-items: center;
    gap: 10px;
    margin-left: -22px;
  }
  .contact__icon { width: 13px; height: 13px; flex: none; }
</style>
</head>
<body>
  <section class="card card--front">
    <div class="mark-decoration" role="img" aria-label="Enlarged silver brand mark decoration"></div>
    <div class="wordmark"><span class="wordmark__dot"></span>galavoyant</div>
  </section>

  <section class="card card--back">
    <div class="wordmark">galavoyant</div>
    <div class="contact">
      <p class="contact__name">Lorna <span class="contact__name-last">Pettibone</span></p>
      <p class="contact__line">PO Box 318,</p>
      <p class="contact__line">Washington, DC 20019</p>
      <p class="contact__line contact__row">
        <svg class="contact__icon" viewBox="0 0 16 16" aria-hidden="true"><path d="M4 1 L6.5 4.5 L5 6 C6 8.5 7.5 10 10 11 L11.5 9.5 L15 12 L13 15 C7 14 2 9 1 3 Z" fill="#5fa9a8"/></svg>
        202.481.7730
      </p>
      <p class="contact__line contact__row">
        <svg class="contact__icon" viewBox="0 0 16 16" aria-hidden="true"><rect x="1" y="3" width="14" height="10" fill="none" stroke="#5fa9a8" stroke-width="1.6"/><path d="M1 3 L8 9 L15 3" fill="none" stroke="#5fa9a8" stroke-width="1.6"/></svg>
        lpettibone@galavoyant.com
      </p>
    </div>
    <div class="mark-decoration" role="img" aria-label="Enlarged silver brand mark decoration"></div>
  </section>
</body>
</html>
```